Showroom Signage Design – Bright Hinges (High-Exposure Road Frontage)

Project Overview
We are looking for a creative designer to develop large-scale external signage for the Bright Hinges showroom.
The building is a double-storey showroom with full glass frontage positioned on a very busy main road.
The glazing spans both levels and we want to utilise the façade like a large billboard that captures attention from passing traffic.
The design must be bold, clean, professional, and highly readable at speed.
About Bright Hinges:
Bright Hinges specialises in cabinetry face-lifts / renovations.
including:
Our Core Service — Cabinetry Facelifts
- Kitchens
- Bathrooms
- Laundries
- Wardrobes
We Also Offer New Installations:
- Kitchens
- Bathrooms
- Laundries
- Wardrobes
We want the signage to clearly communicate that we are experts in facelifting / renovating spaces, while also providing complete new cabinetry solutions.
We will remove the reflective film on the windows for the lower level. There will be a kitchen showing in the middle of the lower level. So we don't want signage infront of the kitchen area. (Attached is a screenshot of the office with blue and pink squares. The blue is the location of the kitchen internally, and the pink can be signage design spaces.) Ideally the printing wont have a solid colour background for printing on the lower level.
Design Goals:
- Turns the entire glazed frontage into a visual billboard
- Works across two storeys
- Is highly visible from passing vehicles
- Uses strong hierarchy and minimal clutter
- Clearly communicates our services at a glance
- Encourages customers to visit the showroom
Think impact first, then detail.
Key Considerations
- Viewed primarily by drive-by traffic
- Must read clearly from distance and speed
- Should utilise window graphics, scale, and layout effectively
- Design should enhance — not block — natural light where possible
- Must feel architectural and professional, not retail clutter
Deliverables:
Print-ready vector files (AI/EPS/PDF)
Building mockups showing real-world application
We are looking for a design that makes Bright Hinges impossible to miss — transforming the showroom frontage into a powerful advertising statement.
Target Market(s)
Renovation clients on a budget, but also clients wanting an efficient turn around of high end projects.
Colors
Designer to choose only greyscale colors for use in the design.
Look and feel

```html
<!DOCTYPE html>
<html lang="en">
<head>
<meta charset="utf-8">
<title>Bright Hinges – Showroom Frontage Signage</title>
<link rel="stylesheet" href="https://fonts.googleapis.com/css2?family=Montserrat:wght@500;600;700;800&family=Jost:wght@400;500;600&display=swap">
<style>
  :root{
    --ink:#2f3032;
    --panel:#35373a;
    --panel-deep:#2a2b2d;
    --glass-top:#4a4c4f;
    --glass-bottom:#6d6f71;
    --band:#dcdcda;
    --paper:#f4f4f2;
    --canvas:#e6e6e3;
    --white:#ffffff;
    --rule:#bfc0c0;
  }
  *{box-sizing:border-box;margin:0;padding:0}
  html,body{width:1200px;height:1200px;overflow:hidden;background:var(--canvas)}
  body{font-family:"Jost",sans-serif;color:var(--white);position:relative}

  .sprite{position:absolute;width:0;height:0;overflow:hidden}
  .icon{width:62px;height:62px;fill:none;stroke:currentColor;stroke-width:2.2;stroke-linecap:round;stroke-linejoin:round}

  .facade{position:absolute;left:40px;top:40px;width:1120px;height:660px}
  .sign{position:absolute;background:var(--panel)}

  /* upper level – main billboard */
  .billboard-main{left:0;top:0;width:520px;height:330px}
  .billboard-main .brand-name{font-family:"Montserrat",sans-serif;font-weight:800;font-size:50px;letter-spacing:.5px;text-align:center;padding-top:30px;line-height:1}
  .billboard-main .tagline{font-family:"Jost",sans-serif;font-weight:500;font-size:17px;letter-spacing:3px;text-align:center;margin-top:18px}
  .service-band{margin-top:22px;background:var(--band);color:var(--ink);text-align:center;font-weight:500;font-size:16px;letter-spacing:3px;padding:10px 0}

  .service-row{display:flex;justify-content:space-around;align-items:stretch;padding:16px 14px 0}
  .service{display:flex;flex-direction:column;align-items:center;gap:8px;font-weight:500;font-size:13px;letter-spacing:.6px;flex:1}
  .service + .service{border-left:1.5px solid var(--rule)}

  /* upper level – centre statement */
  .billboard-expert{left:540px;top:0;width:190px;height:330px;background:linear-gradient(180deg,var(--glass-top),#57595c);padding:60px 20px 0}
  .billboard-expert p{font-weight:500;font-size:17px;letter-spacing:1px;line-height:1.55}
  .billboard-expert .underline{display:block;width:90px;height:2px;background:var(--white);margin-top:14px}

  /* upper level – right billboard */
  .billboard-side{left:750px;top:0;width:370px;height:330px;padding:44px 30px 0}
  .side-name{display:flex;align-items:center;gap:14px;font-family:"Montserrat",sans-serif;font-weight:800;font-size:32px;line-height:1}
  .side-name .mark-square{width:22px;height:22px;border:3px solid var(--white);flex:none}
  .side-list{margin-top:26px;font-weight:500;font-size:15.5px;letter-spacing:2px;line-height:1.75}
  .side-sub{margin-top:22px;font-weight:500;font-size:12.5px;letter-spacing:1.4px;padding-top:14px;border-top:1.5px solid var(--rule)}

  /* lower level – window graphics, no solid print background */
  .window{position:absolute;top:350px;height:310px;background:linear-gradient(180deg,var(--glass-top),var(--glass-bottom))}
  .window-left{left:0;width:520px;padding:50px 30px}
  .window-left .statement{font-weight:500;font-size:25px;letter-spacing:1px;line-height:1.6}
  .window-left .statement-rule{display:block;width:160px;height:2px;background:var(--white);margin-top:16px}
  .window-left .service-note{position:absolute;left:300px;top:56px;width:200px}
  .service-note h3{font-family:"Montserrat",sans-serif;font-weight:800;font-size:20px;letter-spacing:-.3px}
  .service-note p{font-family:"Montserrat",sans-serif;font-weight:500;font-size:14px;line-height:1.25;margin-top:6px}
  .service-note .note-rule{display:block;width:150px;height:1.5px;background:var(--white);margin-top:12px}

  .kitchen-view{position:absolute;left:540px;top:350px;width:190px;height:310px;background:linear-gradient(180deg,#5d5e5f,#a6a39d 60%,#cfcbc3)}

  .window-right{left:750px;width:370px;padding:24px 0 0}
  .window-right .headline{font-weight:500;font-size:16px;letter-spacing:1px;padding:0 24px 14px;border-bottom:1.5px solid var(--rule)}
  .window-right .service-row{padding:18px 6px 0}
  .window-right .service{font-size:11.5px}
  .window-right .icon{width:50px;height:50px}
  .visit-band{position:absolute;left:0;right:0;bottom:22px;background:var(--band);color:var(--ink);font-weight:500;font-size:16px;letter-spacing:1.4px;padding:11px 0;display:flex;justify-content:center;align-items:center;gap:14px}
  .visit-band svg{width:30px;height:14px;stroke:var(--ink);stroke-width:2;fill:none}

  /* brand board */
  .brand-board{position:absolute;left:40px;top:730px;width:1120px;height:430px;background:var(--paper);color:var(--ink)}
  .brand-lockup{position:absolute;left:0;right:0;top:50px;text-align:center}
  .brand-lockup .wordmark{display:inline-flex;align-items:center;gap:20px;font-family:"Montserrat",sans-serif;font-weight:800;font-size:66px;letter-spacing:1px;line-height:1;color:var(--ink)}
  .brand-lockup .mark-square{width:40px;height:40px;border:5px solid var(--ink)}
  .brand-lockup .lockup-rule{width:480px;height:2px;background:var(--ink);margin:26px auto 22px}
  .brand-lockup .lockup-tagline{font-weight:500;font-size:22px;letter-spacing:4px}

  .values{position:absolute;left:0;right:0;bottom:0;height:140px;background:var(--panel-deep);color:var(--white);display:flex;align-items:center;padding:0 40px}
  .value{flex:1;display:flex;flex-direction:column;align-items:center;gap:10px;font-family:"Montserrat",sans-serif;font-weight:600;font-size:13px;letter-spacing:1px;text-align:center;line-height:1.3}
  .value + .value{border-left:1.5px solid #8d8e90}
  .value .icon{width:48px;height:48px}
</style>
</head>
<body>

<svg class="sprite" aria-hidden="true">
  <defs>
    <symbol id="i-kitchen" viewBox="0 0 64 64">
      <rect x="6" y="6" width="52" height="12" rx="1.5"/><line x1="24" y1="6" x2="24" y2="18"/><line x1="40" y1="6" x2="40" y2="18"/>
      <rect x="6" y="34" width="52" height="24" rx="1.5"/><rect x="22" y="38" width="20" height="16"/>
      <line x1="14" y1="40" x2="14" y2="50"/><line x1="50" y1="40" x2="50" y2="50"/>
      <path d="M28 26h8l3 8H25z"/><line x1="32" y1="18" x2="32" y2="26"/>
    </symbol>
    <symbol id="i-bathroom" viewBox="0 0 64 64">
      <rect x="6" y="8" width="18" height="48" rx="3"/><line x1="10" y1="30" x2="14" y2="30"/>
      <path d="M30 12v8M34 10v10h6V10M46 8v14M52 8v14"/>
      <path d="M26 34h34c0 10-6 16-17 16S26 44 26 34z"/><line x1="28" y1="40" x2="58" y2="40"/>
    </symbol>
    <symbol id="i-laundry" viewBox="0 0 64 64">
      <rect x="6" y="6" width="52" height="10" rx="1.5"/><rect x="6" y="20" width="52" height="38" rx="1.5"/>
      <line x1="34" y1="20" x2="34" y2="58"/><circle cx="20" cy="40" r="9"/><circle cx="20" cy="40" r="4.5"/>
      <line x1="40" y1="30" x2="52" y2="30"/><line x1="40" y1="40" x2="52" y2="40"/><line x1="40" y1="50" x2="52" y2="50"/>
      <line x1="10" y1="26" x2="16" y2="26"/>
    </symbol>
    <symbol id="i-wardrobe" viewBox="0 0 64 64">
      <rect x="8" y="4" width="48" height="56" rx="1.5"/>
      <line x1="20" y1="4" x2="20" y2="60"/><line x1="32" y1="4" x2="32" y2="60"/><line x1="44" y1="4" x2="44" y2="60"/>
      <line x1="17" y1="28" x2="17" y2="36"/><line x1="29" y1="28" x2="29" y2="36"/><line x1="35" y1="28" x2="35" y2="36"/><line x1="47" y1="28" x2="47" y2="36"/>
    </symbol>
    <symbol id="i-advice" viewBox="0 0 64 64">
      <path d="M32 8a22 22 0 1 1-12 40l-10 4 4-9A22 22 0 0 1 32 8z"/>
      <circle cx="23" cy="30" r="1.5"/><circle cx="32" cy="30" r="1.5"/><circle cx="41" cy="30" r="1.5"/>
    </symbol>
    <symbol id="i-quality" viewBox="0 0 64 64">
      <path d="M32 6l6 5 8-1 2 8 7 4-3 7 3 7-7 4-2 8-8-1-6 5-6-5-8 1-2-8-7-4 3-7-3-7 7-4 2-8 8 1z"/>
      <path d="M22 32l7 7 13-14"/>
    </symbol>
    <symbol id="i-fast" viewBox="0 0 64 64">
      <circle cx="38" cy="36" r="20"/><line x1="34" y1="8" x2="42" y2="8"/><line x1="38" y1="8" x2="38" y2="16"/>
      <path d="M38 26v10l7 5"/><line x1="4" y1="30" x2="14" y2="30"/><line x1="2" y1="38" x2="14" y2="38"/><line x1="6" y1="46" x2="16" y2="46"/>
    </symbol>
    <symbol id="i-lasting" viewBox="0 0 64 64">
      <path d="M32 6l22 8v16c0 14-10 24-22 28C20 54 10 44 10 30V14z"/>
      <path d="M22 31l7 7 13-14"/>
    </symbol>
  </defs>
</svg>

<section class="facade" aria-label="Showroom frontage signage">

  <div class="sign billboard-main">
    <h1 class="brand-name">BRIGHT HINGES</h1>
    <p class="tagline">FACELIFT. TRANSFORM. LOVE YOUR SPACE.</p>
    <div class="service-band">CABINETRY FACELIFTS</div>
    <ul class="service-row">
      <li class="service"><svg class="icon"><use href="#i-kitchen"/></svg>KITCHENS</li>
      <li class="service"><svg class="icon"><use href="#i-bathroom"/></svg>BATHROOMS</li>
      <li class="service"><svg class="icon"><use href="#i-laundry"/></svg>LAUNDRIES</li>
      <li class="service"><svg class="icon"><use href="#i-wardrobe"/></svg>WARDROBES</li>
    </ul>
  </div>

  <div class="sign billboard-expert">
    <p>EXPERTS IN<br>FACELIFTING<br>&amp; RENOVATING<br>SPACES</p>
    <span class="underline"></span>
  </div>

  <div class="sign billboard-side">
    <div class="side-name"><span class="mark-square"></span>BRIGHT HINGES</div>
    <p class="side-list">KITCHENS. BATHROOMS.<br>LAUNDRIES. WARDROBES.</p>
    <p class="side-sub">FACELIFTS &amp; NEW INSTALLATIONS</p>
  </div>

  <div class="window window-left">
    <p class="statement">NEW LOOK.<br>SAME SPACE.<br>BETTER LIFE.</p>
    <span class="statement-rule"></span>
    <div class="service-note">
      <h3>OUR SERVICE:</h3>
      <p>We make your existing cabinetry new. Fast. Affordable. Professional.</p>
      <span class="note-rule"></span>
    </div>
  </div>

  <div class="kitchen-view" role="img" aria-label="Clear glazing with the display kitchen visible inside the showroom"></div>

  <div class="window window-right">
    <p class="headline">COMPLETE SOLUTIONS. STUNNING RESULTS.</p>
    <ul class="service-row">
      <li class="service"><svg class="icon"><use href="#i-kitchen"/></svg>KITCHENS</li>
      <li class="service"><svg class="icon"><use href="#i-bathroom"/></svg>BATHROOMS</li>
      <li class="service"><svg class="icon"><use href="#i-laundry"/></svg>LAUNDRIES</li>
      <li class="service"><svg class="icon"><use href="#i-wardrobe"/></svg>WARDROBES</li>
    </ul>
    <div class="visit-band">VISIT OUR SHOWROOM TODAY
      <svg viewBox="0 0 30 14"><path d="M1 7h27M21 1l7 6-7 6"/></svg>
    </div>
  </div>

</section>

<section class="brand-board" aria-label="Brand identity">
  <div class="brand-lockup">
    <div class="wordmark"><span class="mark-square"></span>BRIGHT HINGES</div>
    <div class="lockup-rule"></div>
    <p class="lockup-tagline">FACELIFT. TRANSFORM. LOVE YOUR SPACE.</p>
  </div>
  <ul class="values">
    <li class="value"><svg class="icon"><use href="#i-advice"/></svg>EXPERT<br>ADVICE</li>
    <li class="value"><svg class="icon"><use href="#i-quality"/></svg>QUALITY<br>FINISHES</li>
    <li class="value"><svg class="icon"><use href="#i-fast"/></svg>FAST<br>TRANSFORMATION</li>
    <li class="value"><svg class="icon"><use href="#i-lasting"/></svg>MADE TO<br>LAST</li>
  </ul>
</section>

</body>
</html>
```